need a Facebook marketing ad for Korvane Welding

www.korvanewelding.example is our website to look at, I need someone to design a 15-30 second ad video/sideshow for a general welding and fabrication shop, tig welding, trailer repair, build staircases, pipe welding. I don't have the media or the artistic abilities to do it. Attached is what I have, fill in the blanks and add to it.

would like to get
1-2 video ads
1-2 graphic ads
1-2 different yard signs

```html
<!DOCTYPE html>
<html lang="en">
<head>
<meta charset="utf-8">
<title>Korvane Welding – Facebook Ad 1</title>
<link rel="stylesheet" href="https://fonts.googleapis.com/css2?family=Michroma&family=Montserrat:wght@400;500;700;800&display=swap">
<style>
  :root{
    --page:#ffffff;
    --ink:#000000;
    --white:#ffffff;
    --red:#e3262f;
    --red-deep:#8e1116;
    --silver:#c9c9c9;
    --strip:#f1f1f1;
    --badge:#b9bcc2;
    --display:"Michroma", sans-serif;
    --body:"Montserrat", sans-serif;
  }
  *{margin:0;padding:0;box-sizing:border-box}
  html,body{width:1200px;height:1200px;overflow:hidden;background:var(--page)}
  .sheet{position:relative;width:1200px;height:1200px}
  .sheet-title{position:absolute;top:40px;left:0;width:100%;text-align:center;font-family:var(--display);font-size:25px;letter-spacing:3px;color:var(--ink);font-weight:700}
  .ad{position:absolute;left:109px;top:98px;width:1010px;height:1010px;background:var(--ink);overflow:hidden;color:var(--white)}
  .ad-art{position:absolute;inset:0}
  .brand{position:absolute;left:92px;top:128px;width:240px;display:flex;align-items:center;gap:10px}
  .brand-dot{width:34px;height:34px;border-radius:50%;background:var(--red);flex:none}
  .brand-name{font-family:var(--display);font-size:24px;line-height:1.25;color:var(--white)}
  .headline{position:absolute;left:90px;top:494px;font-family:var(--display);font-size:36.5px;line-height:44px;letter-spacing:2px;text-transform:uppercase;white-space:nowrap}
  .tagline{position:absolute;left:93px;top:632px;font-family:var(--body);font-weight:700;font-size:25px;color:var(--red);white-space:nowrap}
  .call-bar{position:absolute;left:68px;top:697px;width:584px;height:67px}
  .call-bar svg{position:absolute;inset:0}
  .call-note{position:absolute;left:25px;top:16px;width:300px;font-family:var(--display);font-size:8.3px;line-height:14px;letter-spacing:.6px;text-transform:uppercase;color:var(--white)}
  .call-icon{position:absolute;left:333px;top:15px;width:33px;height:33px;border-radius:50%;background:var(--red);display:flex;align-items:center;justify-content:center}
  .call-text{position:absolute;left:375px;top:18px;font-family:var(--display);text-transform:uppercase;color:var(--white);white-space:nowrap}
  .call-text .label{display:block;font-size:11px;letter-spacing:1px}
  .call-text .number{display:block;font-size:12.5px;letter-spacing:2.5px;font-weight:700;margin-top:2px}
  .contact{position:absolute;left:95px;top:803px}
  .contact-title{font-family:var(--display);font-size:12.5px;letter-spacing:2.6px;margin-bottom:14px}
  .contact-item{display:flex;align-items:center;gap:9px;font-family:var(--body);font-size:13px;height:24px;white-space:nowrap}
  .contact-item.gap{margin-top:8px}
  .contact-item svg{width:13px;height:13px;flex:none}
  .social{position:absolute;left:94px;top:932px;display:flex;gap:22px}
  .social span{width:13px;height:13px;border-radius:50%;background:var(--white)}
  .services{position:absolute;left:679px;top:597px;width:292px;height:285px}
  .services svg{position:absolute;inset:0}
  .services-title{position:absolute;left:31px;top:29px;font-family:var(--display);font-size:17px;letter-spacing:3px;color:var(--red)}
  .services-list{position:absolute;left:31px;top:66px;list-style:none;font-family:var(--body);font-weight:700;font-size:16px;letter-spacing:.3px}
  .services-list li{height:33.8px;display:flex;align-items:center;white-space:nowrap}
  .services-list li::before{content:"";width:5px;height:5px;border-radius:50%;background:var(--red);margin-right:8px;flex:none}
  .partners{position:absolute;left:291px;top:903px;width:678px;height:60px;background:var(--strip);display:flex;align-items:center;justify-content:space-around}
  .partner{background:var(--badge)}
  .partner.round{width:38px;height:38px;border-radius:50%}
  .partner.square{width:36px;height:36px}
  .copyright{position:absolute;right:41px;top:976px;font-family:var(--body);font-size:9px;color:var(--white)}
</style>
</head>
<body>
<div class="sheet">
  <h1 class="sheet-title">FACEBOOK AD 1</h1>

  <section class="ad">
    <svg class="ad-art" width="1010" height="1010" viewBox="0 0 1010 1010">
      <defs>
        <linearGradient id="photoTone" x1="0" y1="0" x2="1" y2="0.4">
          <stop offset="0" stop-color="#2a211c"/>
          <stop offset="0.35" stop-color="#4a3326"/>
          <stop offset="0.6" stop-color="#3a4a58"/>
          <stop offset="0.8" stop-color="#4b3a2c"/>
          <stop offset="1" stop-color="#252324"/>
        </linearGradient>
        <linearGradient id="edgeLine" x1="0" y1="0" x2="1" y2="0">
          <stop offset="0" stop-color="var(--red-deep)"/>
          <stop offset="1" stop-color="var(--red)"/>
        </linearGradient>
      </defs>
      <polygon points="0,0 1010,0 1010,507 0,382" fill="url(#photoTone)" role="img" aria-label="Photo of a welder in a helmet and leather gloves welding in a workshop with sparks flying"/>
      <line x1="0" y1="382" x2="780" y2="478" stroke="url(#edgeLine)" stroke-width="3"/>
    </svg>

    <div class="brand">
      <span class="brand-dot"></span>
      <span class="brand-name">Korvane<br>Welding</span>
    </div>

    <h2 class="headline">We specialize<br>in welding<br>and fabrication</h2>
    <p class="tagline">If you can dream it, we can build it</p>

    <div class="call-bar">
      <svg width="584" height="67" viewBox="0 0 584 67">
        <defs>
          <linearGradient id="barFill" x1="0" y1="0" x2="1" y2="0">
            <stop offset="0" stop-color="#2b2b2b"/>
            <stop offset="1" stop-color="#0e0e0e"/>
          </linearGradient>
        </defs>
        <polygon points="10,1 583,1 574,66 1,66" fill="url(#barFill)" stroke="var(--silver)" stroke-width="2.5"/>
      </svg>
      <p class="call-note">Please feel free to call or text with any questions we look forward to serving you, sincerely,</p>
      <span class="call-icon">
        <svg width="15" height="15" viewBox="0 0 24 24"><path fill="#fff" d="M6.6 10.8a15.1 15.1 0 0 0 6.6 6.6l2.2-2.2c.3-.3.7-.4 1-.2 1.1.4 2.3.6 3.6.6.6 0 1 .4 1 1V20c0 .6-.4 1-1 1A17 17 0 0 1 3 4c0-.6.4-1 1-1h3.5c.6 0 1 .4 1 1 0 1.3.2 2.5.6 3.6.1.3 0 .7-.2 1z"/></svg>
      </span>
      <div class="call-text">
        <span class="label">Call Now</span>
        <span class="number">555-014-2290</span>
      </div>
    </div>

    <div class="contact">
      <h3 class="contact-title">CONTACT DETAILS</h3>
      <p class="contact-item">
        <svg viewBox="0 0 24 24"><path fill="var(--red)" d="M12 2a7 7 0 0 0-7 7c0 5.3 7 13 7 13s7-7.7 7-13a7 7 0 0 0-7-7zm0 9.5A2.5 2.5 0 1 1 12 6.5a2.5 2.5 0 0 1 0 5z"/></svg>
        Fairhaven TN, 37000
      </p>
      <p class="contact-item">
        <svg viewBox="0 0 24 24"><path fill="var(--red)" d="M6.6 10.8a15.1 15.1 0 0 0 6.6 6.6l2.2-2.2c.3-.3.7-.4 1-.2 1.1.4 2.3.6 3.6.6.6 0 1 .4 1 1V20c0 .6-.4 1-1 1A17 17 0 0 1 3 4c0-.6.4-1 1-1h3.5c.6 0 1 .4 1 1 0 1.3.2 2.5.6 3.6.1.3 0 .7-.2 1z"/></svg>
        555-014-2290
      </p>
      <p class="contact-item gap">
        <svg viewBox="0 0 24 24"><path fill="var(--red)" d="M2 5h20v14H2zm2 2v.5l8 5 8-5V7l-8 5z"/></svg>
        info@korvane.example
      </p>
    </div>

    <div class="social"><span></span><span></span><span></span><span></span></div>

    <aside class="services">
      <svg width="292" height="285" viewBox="0 0 292 285">
        <polygon points="28,0.5 291.5,0.5 291.5,284.5 0.5,284.5 0.5,26" fill="none" stroke="var(--white)" stroke-width="1"/>
      </svg>
      <h3 class="services-title">OUR SERVICES</h3>
      <ul class="services-list">
        <li>Welding &amp; Fabrication</li>
        <li>Cutting</li>
        <li>Mobile Welding</li>
        <li>Welder Testing</li>
        <li>Custom Manufacturing</li>
        <li>Inspection And Consulting</li>
      </ul>
    </aside>

    <div class="partners">
      <span class="partner square"></span>
      <span class="partner round"></span>
      <span class="partner square"></span>
      <span class="partner round"></span>
    </div>

    <p class="copyright">Copyright © 2024 Korvane Welding All Right Reserved.</p>
  </section>
</div>
</body>
</html>
```